Design for a Service-Based Estimate

We want a design for an Estimate that will always be sent in PDF format. The estimate or proposal is a critical document that needs to plainly show the service items, item description but also needs to be attractive and professional looking. Our current estimate deliverable is attached but it looks really basic like a Word document

```html
<!DOCTYPE html>
<html lang="en">
<head>
<meta charset="UTF-8">
<title>Estimate – Keystone Slab</title>
<link rel="stylesheet" href="https://fonts.googleapis.com/css2?family=Open+Sans:wght@400;600;700;800&display=swap">
<style>
  :root {
    --backdrop: #c8c8c8;
    --paper: #ffffff;
    --ink: #1d1d24;
    --navy: #2b2e4c;
    --accent: #d9542a;
    --rule: #cfcfcf;
    --muted: #555;
  }
  * { box-sizing: border-box; margin: 0; padding: 0; }
  html, body {
    width: 1200px; height: 800px; overflow: hidden;
    background: var(--backdrop);
    font-family: "Open Sans", sans-serif;
    color: var(--ink);
  }
  .estimate-page {
    position: absolute; left: 300px; top: 12px;
    width: 600px; height: 776px;
    background: var(--paper);
    padding: 34px 46px 30px 46px;
    font-size: 8.6px; line-height: 1.45;
  }
  .page-header { display: flex; justify-content: space-between; align-items: flex-start; }
  .brand-name {
    margin-top: 60px;
    font-size: 17px; font-weight: 800; letter-spacing: 0.5px;
    color: var(--navy); text-transform: uppercase;
  }
  .recipient { text-align: right; font-size: 9px; line-height: 1.5; }
  .recipient .label { margin-bottom: 4px; }
  .rule { border: 0; border-top: 1px solid var(--rule); }
  .header-rule { margin-top: 22px; }
  .project { text-align: center; margin: 16px 0 18px; font-size: 8.6px; line-height: 1.6; }
  .project .project-title { font-weight: 700; }
  .line-items { width: 100%; border-collapse: collapse; }
  .line-items th {
    font-weight: 700; color: var(--navy); font-size: 9px;
    text-align: left; padding: 6px 6px 6px 0; vertical-align: bottom;
    border-bottom: 1px solid var(--rule);
  }
  .line-items td { padding: 9px 6px 9px 0; vertical-align: top; border-bottom: 1px solid #e4e4e4; }
  .line-items .num { text-align: center; }
  .line-items .money { text-align: right; }
  .line-items .total { text-align: right; font-weight: 700; font-size: 9.6px; }
  .line-items .col-item { width: 54%; }
  .line-items .total-row td { border-bottom: 0; font-weight: 700; }
  .terms { margin-top: 30px; }
  .terms h2 { text-align: center; font-size: 11px; font-weight: 600; margin-bottom: 10px; }
  .terms ul { padding-left: 14px; font-size: 8px; line-height: 1.5; }
  .terms li { margin-bottom: 1px; }
  .terms-rule { margin-top: 18px; }
  .signatures { margin-top: 30px; width: 220px; }
  .sign-line { border-top: 1px solid var(--ink); padding-top: 3px; font-size: 9px; margin-bottom: 30px; }
</style>
</head>
<body>
  <main class="estimate-page">
    <header class="page-header">
      <div class="brand-name">Keystone Slab</div>
      <address class="recipient" style="font-style:normal">
        <div class="label">To:</div>
        <div>Dale Harrow</div>
        <div>48 Marlow Lane SE Fairhaven 30412</div>
        <div>dharrow@mailbox.example</div>
      </address>
    </header>
    <hr class="rule header-rule">

    <section class="project">
      <div class="project-title">Dale Harrow New Concrete Pad</div>
      <div>48 Marlow Lane SE Fairhaven 30412</div>
      <div>Bid#: 20-0182</div>
    </section>

    <table class="line-items">
      <thead>
        <tr>
          <th class="col-item">Item</th>
          <th class="num">Quantity</th>
          <th class="num">U/M</th>
          <th class="money">Unit<br>$</th>
          <th class="money">Total $</th>
        </tr>
      </thead>
      <tbody>
        <tr>
          <td>Form, Pour &amp; Finish New Concrete Slab (24' x 24' x 4"). Includes: 3000psi Concrete Mix, Footer (12" x 8") with One (#5) Continuous Rebar, Wire Mesh Reinforcement and Saw-Cut Expansion Joints</td>
          <td class="num">576</td>
          <td class="num">SF</td>
          <td class="money">$8.65</td>
          <td class="total">$4,982.40</td>
        </tr>
        <tr>
          <td>OPTIONAL: Add (2' x 24' x 4") Small Ramp Area</td>
          <td class="num">48</td>
          <td class="num">SF</td>
          <td class="money">$8.65</td>
          <td class="total">$415.20</td>
        </tr>
        <tr class="total-row">
          <td></td><td></td>
          <td colspan="2" class="money">Total Price</td>
          <td class="total">$5,397.60</td>
        </tr>
      </tbody>
    </table>

    <section class="terms">
      <h2>Terms and Conditions</h2>
      <ul>
        <li>Prices as quoted in this estimate are valid for (60) days only.</li>
        <li>Payment in full, less any previously paid amounts, is due to the Contractor upon completion of the proposed scope of work.</li>
        <li>All change order requests must be communicated in writing to the Contractor by the Client or their authorized representative.</li>
        <li>All measurements listed in this estimate are approximate and may vary slightly due to actual field conditions.</li>
        <li>It is agreed by the Contractor and the Client that complications and costs arising from unforeseen conditions and handling of unsuitable materials are not included in this estimate.</li>
        <li>Unless specifically listed in this estimate, the following items and their costs are not included: Maintenance of Traffic, Concrete Material Pumping, Testing, Excavation, Grading and Fill Material, Permits and Fees, Surveying and As-builts, Irrigation Repair, Landscaping and Root Mitigation, De-watering, Private Locates and Accessibility.</li>
        <li>Private utility locating services using radio detection devices and, when necessary, ground penetrating radar are offered by Keystone Slab to assist in finding private utilities that may not have been located by the public one call system. Keystone Slab will not be responsible for private utilities that have not been located nor for the failure of the above equipment to accurately detect existing utilities since the equipment is fallible and existing site conditions may preclude the ability of the equipment to detect an identifiable signal.</li>
      </ul>
      <hr class="rule terms-rule">
    </section>

    <section class="signatures">
      <div class="sign-line">Client Signature</div>
      <div class="sign-line">Date</div>
    </section>
  </main>
</body>
</html>
```